Wound Care Flyer

Looking for a Trifold brochure that is modern and has a high aesthetic. (Specialty services) Would like the colors to center around Black and Gold. Possibly updating the logo. Attached is the old brochure and a document about our services.

```html
<!DOCTYPE html>
<html lang="en">
<head>
<meta charset="utf-8">
<title>Cedarline Wounds – Trifold Brochure</title>
<link href="https://fonts.googleapis.com/css2?family=Zilla+Slab:wght@500;600;700&family=Lato:wght@400;700&family=Great+Vibes&display=swap" rel="stylesheet">
<style>
  :root{
    --black:#151414;
    --ink:#1d1b1a;
    --white:#ffffff;
    --gold-dark:#7a5a2e;
    --gold:#b48a4e;
    --gold-light:#ecd49c;
    --brown:#8e5a2a;
    --head-gold:#caa46a;
    --page:#ffffff;
  }
  *{box-sizing:border-box;margin:0;padding:0}
  html,body{width:1078px;height:1200px;overflow:hidden;background:var(--page)}
  body{font-family:"Lato",Arial,sans-serif;color:var(--ink)}
  .spread{position:absolute;left:169px;width:740px;height:572px;overflow:hidden;background:var(--black);box-shadow:0 2px 8px rgba(0,0,0,.25)}
  .spread--outside{top:20px}
  .spread--inside{top:608px}
  .spread svg.bg{position:absolute;left:0;top:0}
  .block{position:absolute}
  .h-panel{font-family:"Zilla Slab",Georgia,serif;font-weight:600;font-size:24px;line-height:22px;
    background:linear-gradient(90deg,#a7773f,#e2c48a);-webkit-background-clip:text;background-clip:text;color:transparent}
  .h-dark{color:var(--black);background:none;-webkit-background-clip:border-box;background-clip:border-box}
  .body{font-size:10px;line-height:11.6px;color:var(--white)}
  .body.dark{color:var(--ink)}
  .body p+p{margin-top:9px}
  .sub{font-family:"Zilla Slab",Georgia,serif;font-weight:600;font-size:14.5px;line-height:12px;color:var(--brown)}
  .sub.gold{color:var(--head-gold)}
  .kicker{font-size:10.5px;color:var(--brown);font-weight:700}
  .kicker-title{font-family:"Zilla Slab",Georgia,serif;font-weight:700;font-size:14.5px;color:var(--ink)}
  .bullets{list-style:none}
  .bullets li{position:relative;padding-left:15px;font-size:10px;line-height:17px}
  .bullets li::before{content:"";position:absolute;left:2px;top:5.5px;width:6px;height:6px;border-radius:50%;background:var(--gold);box-shadow:0 0 0 1.5px rgba(180,138,78,.35)}
  .bullets.dark li{color:var(--ink)}
  .bullets.light li{color:var(--white)}
  .bullets.tight li{line-height:13px;margin-bottom:5px}
  .feature{position:absolute;left:17px;width:200px}
  .feature .f-head{display:flex;align-items:flex-start;gap:5px}
  .feature .f-text{font-size:9.6px;line-height:11px;margin-top:4px;color:var(--ink)}
  .contact-title{font-family:"Zilla Slab",Georgia,serif;font-weight:600;font-size:25px;color:var(--black)}
  .contact-line{display:flex;align-items:center;gap:5px;font-size:15px;color:var(--white);line-height:21px}
  .contact-line.small{font-size:12.5px}
  .brand-name{font-family:"Zilla Slab",Georgia,serif;font-weight:500;font-size:17px;letter-spacing:3px;color:var(--head-gold);text-align:center;line-height:22px}
  .script{font-family:"Great Vibes",cursive;font-size:34px;color:var(--white);text-align:center}
  .hero-title{font-family:"Zilla Slab",Georgia,serif;font-weight:600;font-size:28px;color:var(--head-gold);text-align:center}
  .name-plate{font-family:"Zilla Slab",Georgia,serif;font-weight:600;font-size:13px;color:var(--black);text-align:center;line-height:28px}
  .cols{display:flex;gap:18px}
  .rule{position:absolute;height:1.5px;background:var(--black)}
</style>
</head>
<body>

<!-- OUTSIDE SPREAD -->
<section class="spread spread--outside">
  <svg class="bg" width="740" height="572" viewBox="0 0 740 572">
    <defs>
      <linearGradient id="goldA" x1="0" y1="1" x2="1" y2="0">
        <stop offset="0" stop-color="#7a5a2e"/><stop offset=".5" stop-color="#b89158"/><stop offset="1" stop-color="#ecd49c"/>
      </linearGradient>
      <linearGradient id="goldB" x1="0" y1="0" x2="1" y2="0">
        <stop offset="0" stop-color="#8c6a38"/><stop offset="1" stop-color="#e9cf97"/>
      </linearGradient>
      <linearGradient id="photoSkin" x1="0" y1="0" x2="1" y2="1">
        <stop offset="0" stop-color="#e9e4df"/><stop offset=".5" stop-color="#a8694a"/><stop offset="1" stop-color="#5a3424"/>
      </linearGradient>
      <linearGradient id="photoClinic" x1="0" y1="0" x2="0" y2="1">
        <stop offset="0" stop-color="#dfe5ea"/><stop offset=".6" stop-color="#f2f2f2"/><stop offset="1" stop-color="#cdb7c4"/>
      </linearGradient>
    </defs>
    <!-- panel 1 white card -->
    <path d="M0 192 H187 A40 40 0 0 1 227 232 V572 H0 Z" fill="#ffffff"/>
    <path d="M150 192 H187 A40 40 0 0 1 227 232 V572" fill="none" stroke="url(#goldB)" stroke-width="1.5"/>
    <circle cx="205" cy="206" r="16" fill="url(#goldA)"/>
    <!-- panel 2 gold arch -->
    <path d="M244 572 V224 A123.5 123.5 0 0 1 491 224 V572 Z" fill="url(#goldA)"/>
    <path d="M244 418 Q367 385 491 405 V414 Q367 394 244 428 Z" fill="#151414"/>
    <path d="M244 428 Q367 396 491 414 V421 Q367 402 244 436 Z" fill="#ffffff"/>
    <circle cx="367" cy="116" r="90" fill="none" stroke="url(#goldB)" stroke-width="2"/>
    <circle cx="367" cy="116" r="85" fill="url(#photoSkin)" role="img" aria-label="Photo: clinician dressing a patient's knee wound"/>
    <circle cx="470" cy="230" r="14" fill="url(#goldA)"/>
    <!-- panel 3 frame lines -->
    <path d="M722 0 V140 A30 30 0 0 1 692 170 H540" fill="none" stroke="url(#goldB)" stroke-width="1.5"/>
    <circle cx="617" cy="72" r="48" fill="none" stroke="url(#goldB)" stroke-width="2"/>
    <path d="M520 555 V385 A86 86 0 0 1 606 299" fill="none" stroke="url(#goldB)" stroke-width="1.5"/>
    <path d="M529 555 V382 A84.5 84.5 0 0 1 698 382 V555 Z" fill="url(#photoClinic)" role="img" aria-label="Portrait photo of the nurse practitioner in a white coat"/>
    <circle cx="698" cy="343" r="14" fill="url(#goldA)"/>
    <rect x="553" y="509" width="169" height="28" fill="url(#goldB)"/>
  </svg>

  <!-- panel 1 -->
  <h2 class="block h-panel" style="left:17px;top:16px;width:210px">Personalized<br>Care Plans</h2>
  <div class="block body" style="left:17px;top:72px;width:200px;font-size:9.6px;line-height:11px">
    <p>Customized care plans designed to meet the specific needs of each patient, ensuring optimal healing. Coordination and direction of care for other caregivers and clinicians, including home health.</p>
    <p>Patient and Caregiver Education Providing education and support to patients and their caregivers to enhance understanding and promote self-care.</p>
  </div>
  <div class="block" style="left:17px;top:206px">
    <div class="kicker">Partner with</div>
    <div class="kicker-title">Cedarline Wounds:</div>
  </div>

  <div class="feature" style="top:244px">
    <div class="f-head">
      <svg width="16" height="18" viewBox="0 0 16 18"><rect x="1" y="1" width="14" height="16" rx="2" fill="none" stroke="#151414" stroke-width="2"/><path d="M4 6h8M4 10h8M4 14h5" stroke="#151414" stroke-width="1.5"/></svg>
      <div class="sub">Enhanced Patient<br>Outcomes</div>
    </div>
    <p class="f-text">Our specialized expertise in advanced wound care leads to faster healing times and improved patient satisfaction.</p>
  </div>
  <div class="feature" style="top:318px">
    <div class="f-head">
      <svg width="18" height="18" viewBox="0 0 18 18"><circle cx="9" cy="5" r="3" fill="#151414"/><path d="M3 17c0-4 3-7 6-7s6 3 6 7z" fill="#151414"/><path d="M1 5l2 3M17 5l-2 3" stroke="#151414" stroke-width="1.5"/></svg>
      <div class="sub">Extended<br>Reach</div>
    </div>
    <p class="f-text">Our in-home services allow your patients to receive high-quality care without the need for frequent visits, reducing the burden on your resources.</p>
  </div>
  <div class="feature" style="top:401px">
    <div class="f-head">
      <svg width="18" height="18" viewBox="0 0 18 18"><circle cx="9" cy="5" r="4" fill="#151414"/><path d="M2 17c0-4 3-6 7-6s7 2 7 6z" fill="#151414"/></svg>
      <div class="sub">Professional<br>Integrity</div>
    </div>
    <p class="f-text">As a trusted partner, we uphold the highest standards of care and professionalism, reflecting positively on your clinic's reputation.</p>
  </div>
  <div class="feature" style="top:489px">
    <div class="f-head">
      <svg width="18" height="18" viewBox="0 0 18 18"><path d="M6 1h6v5h5v6h-5v5H6v-5H1V6h5z" fill="#151414"/></svg>
      <div class="sub">Seamless<br>Collaboration</div>
    </div>
    <p class="f-text">We maintain open communication with referring clinics, ensuring a coordinated approach to patient care.</p>
  </div>

  <!-- panel 2 -->
  <h3 class="block" style="left:262px;top:226px;width:220px;font-family:'Zilla Slab',Georgia,serif;font-weight:600;font-size:14.5px;line-height:15px;color:var(--black)">Specializing in Biologic Skin Substitutes to Treat:</h3>
  <ul class="block bullets light" style="left:262px;top:270px;width:220px">
    <li>Pressure Injuries</li>
    <li>Surgical and Trauma Wounds</li>
    <li>Venous and Arterial Wounds</li>
    <li>Diabetic Wounds</li>
    <li>Diagnostic Testing</li>
    <li>Debridements</li>
    <li>Multidisciplinary Collaboration</li>
  </ul>
  <div class="block" style="left:262px;top:466px;width:225px">
    <h3 class="contact-title">Contact Us</h3>
    <div class="contact-line"><svg width="11" height="11" viewBox="0 0 12 12"><path d="M2 1l2.5 0 1 3-1.5 1a7 7 0 0 0 3 3l1-1.5 3 1V10a1.5 1.5 0 0 1-1.5 1.5A10 10 0 0 1 .5 2.5 1.5 1.5 0 0 1 2 1z" fill="#151414"/></svg>(555) 210-4418</div>
    <div class="contact-line"><svg width="11" height="11" viewBox="0 0 12 12"><rect x="1" y="2" width="10" height="9" rx="1" fill="#151414"/><rect x="3" y="4" width="6" height="2" fill="#c9a36a"/></svg>(555) 309-7725</div>
    <div class="contact-line small"><svg width="11" height="9" viewBox="0 0 12 9"><rect x="0" y="0" width="12" height="9" fill="#151414"/><path d="M0 0l6 5 6-5" stroke="#c9a36a" fill="none"/></svg>CedarlineWounds@example.com</div>
  </div>

  <!-- panel 3 -->
  <div class="block brand-name" style="left:517px;top:132px;width:200px">CEDARLINE<br>WOUNDS</div>
  <div class="block script" style="left:510px;top:214px;width:215px">Advanced</div>
  <div class="block hero-title" style="left:498px;top:258px;width:240px">Wound Care</div>
  <div class="block name-plate" style="left:553px;top:509px;width:169px">Dana Mercer, FNP-C</div>
</section>

<!-- INSIDE SPREAD -->
<section class="spread spread--inside">
  <svg class="bg" width="740" height="572" viewBox="0 0 740 572">
    <defs>
      <linearGradient id="goldC" x1="0" y1="1" x2="1" y2="0">
        <stop offset="0" stop-color="#7a5a2e"/><stop offset=".55" stop-color="#b89158"/><stop offset="1" stop-color="#ecd49c"/>
      </linearGradient>
      <linearGradient id="goldD" x1="0" y1="0" x2="1" y2="0">
        <stop offset="0" stop-color="#8c6a38"/><stop offset="1" stop-color="#e9cf97"/>
      </linearGradient>
      <linearGradient id="photoKnee" x1="0" y1="0" x2="1" y2="1">
        <stop offset="0" stop-color="#efe9e4"/><stop offset=".5" stop-color="#b4785a"/><stop offset="1" stop-color="#6a3e2b"/>
      </linearGradient>
      <linearGradient id="photoHands" x1="0" y1="0" x2="0" y2="1">
        <stop offset="0" stop-color="#8a2a2a"/><stop offset=".5" stop-color="#b4765a"/><stop offset="1" stop-color="#5e3524"/>
      </linearGradient>
    </defs>
    <!-- panel 1 -->
    <path d="M0 0 H229 V332 A40 40 0 0 1 189 372 H0 Z" fill="#ffffff"/>
    <path d="M229 250 V332 A40 40 0 0 1 189 372 H120" fill="none" stroke="url(#goldD)" stroke-width="1.5"/>
    <circle cx="202" cy="363" r="16" fill="url(#goldC)"/>
    <path d="M36 572 V480 A80 80 0 0 1 116 400" fill="none" stroke="url(#goldD)" stroke-width="1.5"/>
    <path d="M46 572 V480 A79.5 79.5 0 0 1 205 480 V572 Z" fill="url(#photoKnee)" role="img" aria-label="Photo: cleaning a wound on a patient's knee"/>
    <!-- panel 2 -->
    <path d="M243 0 H491 V332 A124 124 0 0 1 243 332 Z" fill="url(#goldC)"/>
    <circle cx="367" cy="455" r="91" fill="none" stroke="url(#goldD)" stroke-width="2"/>
    <circle cx="367" cy="455" r="86" fill="url(#photoHands)" role="img" aria-label="Photo: hands applying a dressing to a knee wound"/>
    <circle cx="246" cy="352" r="13" fill="#151414"/>
    <!-- panel 3 bottom swoosh -->
    <circle cx="548" cy="526" r="12" fill="url(#goldC)"/>
    <path d="M548 572 Q620 500 740 484 V492 Q626 508 560 572 Z" fill="url(#goldD)"/>
    <path d="M566 572 Q630 514 740 500 V506 Q636 520 576 572 Z" fill="#ffffff"/>
  </svg>

  <!-- panel 1 -->
  <h2 class="block h-panel" style="left:17px;top:16px;width:200px">About Us</h2>
  <div class="block body dark" style="left:17px;top:54px;width:200px">
    <p>We provide an additional layer of expertise by utilizing advanced the advanced technology of biological skin substitute grafts.</p>
    <p>We pride ourselves in working in close coordination with the patient's care team,including home health services and the primary care physician (PcP).</p>
    <p>We ensure seamless integration without duplicating services prioritizing collaborative care, sharing detailed notes and working closely with the patient's home health team on days between visits.</p>
  </div>
  <div class="block" style="left:17px;top:250px">
    <div class="kicker">Serving the greater</div>
    <div class="kicker-title">North Houston area.</div>
  </div>
  <div class="block cols" style="left:17px;top:282px">
    <ul class="bullets dark"><li>Spring</li><li>Tomball</li><li>Willis</li><li>Montgomery</li></ul>
    <ul class="bullets dark"><li>The Woodlands</li><li>Conroe</li><li>Magnolia</li><li>Cypress</li></ul>
  </div>
  <div class="rule" style="left:0;top:360px;width:110px"></div>

  <!-- panel 2 -->
  <h2 class="block h-panel h-dark" style="left:260px;top:16px;width:220px">Mobile Wound<br>Care</h2>
  <div class="block body" style="left:260px;top:80px;width:222px">
    <p>With a focus on convenience, expertise, and compassion, we bring the highest standard of wound care directly to the patient's home. Working side-by-side with the patient's physician, our team of experienced specialists utilize cutting-edge technology and personalized treatment plans to ensure optimal healing and comfort. From thorough wound assessments to advanced therapies and ongoing support, we prioritize the well-being of our patients every step of the way. Whether it's managing chronic wounds, post-surgery recovery, we go above and beyond to provide comprehensive and compassionate care. With our concierge approach, we aim to make the healing journey as seamless and comfortable as possible, empowering our patients to live their best lives.</p>
  </div>

  <!-- panel 3 -->
  <h2 class="block h-panel" style="left:508px;top:16px;width:225px">Leaders in<br>Mobile Advanced<br>Wound Care.</h2>
  <div class="block body" style="left:508px;top:105px;width:215px">
    <p>We provide a complete wound management program for our patients that includes the use of advanced treatments, the creation of care plans, and coordination of care with other clinicians. Our comprehensive in-home wound care services include:</p>
  </div>
  <div class="block sub gold" style="left:508px;top:200px">Advanced Wound<br>Assessmen</div>
  <ul class="block bullets light tight" style="left:510px;top:233px;width:205px">
    <li>Thorough evaluation of wound type, size, and stage to develop a tailored treatment plan.</li>
  </ul>
  <div class="block sub gold" style="left:508px;top:282px">Cutting-Edge<br>Treatments</div>
  <ul class="block bullets light" style="left:510px;top:313px;width:215px">
    <li style="line-height:13px;margin-bottom:4px">Utilization of the latest technologies and techniques in wound care, including:</li>
    <li>Compression</li>
    <li>Biologic Skin Substitutes</li>
    <li>Negative Pressure Wound Therapy</li>
    <li>Collagen and Advanced Dressings</li>
    <li>Surgical/ Trauma Wounds</li>
    <li>Venous/ Arterial Wounds</li>
    <li>Debridements</li>
  </ul>
</section>

</body>
</html>
```